Chai Tea Company needs a Tea Packaging Box Design

Tea Packaging
Dimensions of the Tea Packaging Box: Height 13 cm; Width 8.5 cm; Depth 7 cm
Individual Teabag Packet/ Sachet: Width 6.5 cm; Length 8.25 cm
We are looking for a new tea packaging design, for our tea business. The material of the box is cardboard. We are also looking for a design that will be on each individual tea bag sachet/packet that goes into the box. This design will be very similar to what you design for the tea packaging box.
Product Info:
Our tea company is called “Marlow Loft”. We sell two types of Chai Tea, once called “Ember Blend” and one called “Meadow Tisane”. The Ember Blend has caffeine, while the Meadow Tisane is Naturally Caffeine Free. The Ember Blend has a black tea base, while the Meadow Tisane has a Rooibos tea base. We will need two tea packaging designs, one for each Chai Tea flavour. The designs for both the teas can be similar, but make sure that you can easily distinguish one from the other (example: make them have different colours or pictures). Both the chai teas, come from the same product line.
Tea Packaging Design:
We are looking for high end tea packaging. We produce high quality teas, and we would like to portray this in our tea packaging. Our teas are made with no artificial flavourings, natural flavourings, or preservatives, so we would also like a natural, organic, high quality look to our tea packaging. Our current logo is a llama. It would be great if you could make the current logo more polished and well made. If you feel that the llama is not well suited or you would like to design the llama differently, we are open to your creative ideas.
General Basic Info:
Keep in mind, we will have both English and French writing on the tea packaging. You do not need to worry about the French writing (we will do the translation), just make sure there is room for it. However, if you feel that you are capable and knowledgeable of incorporating both French and English language into the tea packaging that would be of great help and value.
Back of the Box:
- Will have ingredients and brewing instructions. Basic brewing instructions are: “Add hot water to teabag. Steep for 5-7 minutes, depending on strength preferred. Add milk and your choice of sweetener. Enjoy! See inside panel of box for more detailed instructions”. (The basic brewing instructions, can further be polished or written in a more creative or professional manner).
Front of the Box:
- Will have company name, type of tea, little description of the tea
- 18 teabags
- 54 g (1.9 OZ)
- Should state that this is a product of Alberta, Canada.
Side of the Box:
Any creative wording, slogan, or description about the tea, or whatever you feel would be good on the side of the box.
On the inside flap of the side of the box, there will be detailed instructions on how to brew the tea. These will be different from the simplified brewing instructions on the back of the box. I have attached the advanced brewing instructions as a file. These instructions can further be simplified or reduced to make it easier and cleaner for the consumers to read.
Individual Tea Sachets/ Packets
- These will have a matching look and design of the tea box packaging, except on a smaller scale. Each individual sachet will have the company name, type of tea, little description of the tea in the front of the sachet, while the back will contain the ingredients, and basic brewing instructions.
I have attached a few files, with the dimensions, ingredients, detailed brewing directions, and current logo of the business.
If you have any questions, about the design or packaging please let me know. The winning designer will be required to do a few additional tweaks to finalize the product. Thank you for your time and happy designing!

```html
<!DOCTYPE html>
<html lang="en">
<head>
<meta charset="utf-8">
<title>Marlow Loft – Tea Packaging</title>
<link rel="stylesheet" href="https://fonts.googleapis.com/css2?family=Fredoka:wght@600&family=Caveat+Brush&family=Alegreya:ital,wght@0,400;1,400&family=Source+Sans+3:wght@400;700&display=swap">
<style>
  :root {
    --backdrop: #2b2723;
    --paper: #efede4;
    --seal: #f8f7f2;
    --green: #2f6b2a;
    --green-deep: #245321;
    --brown: #3a2a18;
    --brown-deep: #2c1f11;
    --orange: #d9822b;
    --ink-light: #f4f1e6;
    --font-brand: "Fredoka", "Arial Rounded MT Bold", sans-serif;
    --font-variety: "Caveat Brush", cursive;
    --font-body: "Alegreya", Georgia, serif;
    --font-list: "Source Sans 3", Arial, sans-serif;
  }
  * { box-sizing: border-box; margin: 0; padding: 0; }
  html, body { width: 1200px; height: 900px; overflow: hidden; background: var(--backdrop); }
  .canvas { position: relative; width: 1200px; height: 900px; overflow: hidden; background: var(--backdrop); }

  .pack--meadow { --tone: var(--green); --tone-deep: var(--green-deep); --badge: var(--brown); }
  .pack--ember  { --tone: var(--brown); --tone-deep: var(--brown-deep); --badge: var(--orange); }

  /* Box front panel */
  .box-front {
    position: absolute; top: 40px; width: 300px; height: 460px;
    background: var(--paper); overflow: hidden;
  }
  .box-front.pack--meadow { left: 285px; }
  .box-front.pack--ember { left: 615px; }
  .pattern-band { position: absolute; background: var(--tone); }
  .box-front .pattern-band { left: 45px; top: 0; width: 210px; height: 200px; }
  .base-band { position: absolute; background: var(--tone-deep); }
  .box-front .base-band { left: 55px; top: 345px; right: 0; bottom: 0; }

  .seal {
    position: absolute; border-radius: 50%; background: var(--seal);
    display: flex; flex-direction: column; align-items: center; text-align: center;
    color: var(--tone);
  }
  .seal::before {
    content: ""; position: absolute; inset: 7px; border-radius: 50%;
    border: 2px dotted var(--tone); opacity: .7;
  }
  .box-front .seal { left: 22px; top: 108px; width: 256px; height: 256px; padding-top: 40px; }
  .brand { font-family: var(--font-brand); font-weight: 600; color: var(--tone); line-height: 1; }
  .box-front .brand { font-size: 27px; }
  .seal-rule { border: 0; border-top: 2px solid var(--tone); }
  .box-front .seal-rule { width: 200px; margin: 10px 0 4px; }
  .variety { font-family: var(--font-variety); font-weight: 400; line-height: 1; color: var(--tone); }
  .box-front .variety { font-size: 40px; }
  .desc { font-family: var(--font-body); color: var(--brown-deep); line-height: 1.2; }
  .box-front .desc { font-size: 11px; width: 200px; }
  .dots { font-size: 8px; color: var(--tone); letter-spacing: 3px; line-height: 1.3; }

  .badge {
    position: absolute; border-radius: 50%; background: var(--badge);
    color: var(--ink-light); display: flex; flex-direction: column; align-items: center; justify-content: center;
    font-family: var(--font-body); line-height: 1;
  }
  .box-front .badge { left: 238px; top: 330px; width: 48px; height: 48px; border: 2px solid var(--paper); }
  .badge span { font-size: 6.5px; }
  .badge b { font-family: var(--font-list); font-size: 15px; font-weight: 700; }

  .origin { position: absolute; left: 70px; font-family: var(--font-body); font-size: 13px; color: var(--ink-light); }
  .origin--en { top: 393px; }
  .origin--fr { top: 425px; }
  .origin-rule { position: absolute; left: 70px; top: 416px; width: 170px; border: 0; border-top: 1px solid var(--ink-light); opacity: .6; }
  .weight { position: absolute; left: 10px; top: 398px; font-family: var(--font-body); font-size: 13px; color: var(--brown-deep); line-height: 1.2; text-align: center; }

  /* Sachets */
  .sachet {
    position: absolute; top: 545px; width: 220px; height: 279px;
    background: var(--paper); overflow: hidden;
  }
  .sachet--meadow-front { left: 115px; }
  .sachet--meadow-back { left: 365px; }
  .sachet--ember-front { left: 615px; }
  .sachet--ember-back { left: 865px; }
  .sachet .pattern-band { left: 45px; top: 0; width: 130px; height: 95px; }
  .sachet .seal { left: 18px; top: 62px; width: 184px; height: 184px; padding-top: 30px; }
  .sachet .seal::before { inset: 5px; }
  .sachet .brand { font-size: 19px; }
  .sachet .seal-rule { width: 140px; margin: 6px 0 2px; border-top-width: 1.5px; }
  .sachet .variety { font-size: 27px; }
  .sachet .desc { font-size: 6.6px; width: 140px; margin-top: 3px; }

  .recipe { padding: 16px 16px 0; font-family: var(--font-list); color: var(--brown-deep); }
  .recipe h3 { font-size: 10px; font-weight: 700; color: var(--tone); margin-bottom: 3px; }
  .recipe ul { list-style: none; }
  .recipe li { position: relative; font-size: 8.6px; line-height: 1.25; padding-left: 13px; margin-bottom: 1px; }
  .recipe li::before {
    content: ""; position: absolute; left: 1px; top: 2px; width: 7px; height: 7px;
    background: var(--tone); border-radius: 0 60% 0 60%;
  }
  .recipe hr { border: 0; border-top: 1px solid var(--tone); margin: 8px 0; opacity: .7; }
</style>
</head>
<body>
<main class="canvas">

  <article class="box-front pack--meadow">
    <div class="pattern-band" role="img" aria-label="Green leaf pattern texture"></div>
    <div class="base-band"></div>
    <div class="seal">
      <p class="brand">Marlow Loft</p>
      <hr class="seal-rule">
      <h2 class="variety">Meadow Tisane</h2>
      <hr class="seal-rule" style="margin:4px 0 8px">
      <p class="desc">CHAI is a rich blend of strong and flavourful tea, aromatic spices, milk and sugar.</p>
      <p class="dots">• • •</p>
      <p class="desc">CHAI est un riche mélange de thé fort et savoureux, aromates, le lait et le sucre.</p>
    </div>
    <div class="badge"><span>teabags</span><b>18</b><span>sachets de thé</span></div>
    <p class="origin origin--en">Product of Alberta, Canada</p>
    <hr class="origin-rule">
    <p class="origin origin--fr">Produit de l'Alberta, Canada</p>
    <p class="weight">54 g<br>1.9 OZ</p>
  </article>

  <article class="box-front pack--ember">
    <div class="pattern-band" role="img" aria-label="Dark brown leaf pattern texture"></div>
    <div class="base-band"></div>
    <div class="seal">
      <p class="brand">Marlow Loft</p>
      <hr class="seal-rule">
      <h2 class="variety">Ember Blend</h2>
      <hr class="seal-rule" style="margin:4px 0 8px">
      <p class="desc">CHAI is a rich blend of strong and flavourful tea, aromatic spices, milk and sugar.</p>
      <p class="dots">• • •</p>
      <p class="desc">CHAI est un riche mélange de thé fort et savoureux, aromates, le lait et le sucre.</p>
    </div>
    <div class="badge"><span>teabags</span><b>18</b><span>sachets de thé</span></div>
    <p class="origin origin--en">Product of Alberta, Canada</p>
    <hr class="origin-rule">
    <p class="origin origin--fr">Produit de l'Alberta, Canada</p>
    <p class="weight">54 g<br>1.9 OZ</p>
  </article>

  <article class="sachet sachet--meadow-front pack--meadow">
    <div class="pattern-band" role="img" aria-label="Green leaf pattern texture"></div>
    <div class="seal">
      <p class="brand">Marlow Loft</p>
      <hr class="seal-rule">
      <h2 class="variety">Meadow Tisane</h2>
      <p class="desc">CHAI is a rich blend of strong and flavourful tea, aromatic spices, milk and sugar. Authentic Chai is an art that requires all natural ingredients, care and time to prepare.</p>
      <p class="desc">CHAI est un riche mélange de thé fort et savoureux, aromates, le lait et le sucre.</p>
    </div>
  </article>

  <article class="sachet sachet--meadow-back pack--meadow">
    <div class="recipe">
      <h3>INGREDIENTS /for 2 cups/:</h3>
      <ul>
        <li>1½ cups (12 oz) water.</li>
        <li>2 Chai tea bags.</li>
        <li>1 cup (8oz) (whole) milk.</li>
        <li>2-4 teaspoons sugar<br>or honey to taste</li>
        <li>1-2 teaspoons of sliced<br>or grated fresh ginger (optional)</li>
      </ul>
      <hr>
      <h3>INGRÉDIENTS /pour 2 tasses/:</h3>
      <ul>
        <li>1½ tasse (12 oz) d'eau.</li>
        <li>2 sachets de thé Chai.</li>
        <li>1 tasse (8 onces) (ensemble) lait.</li>
        <li>2-4 cuillères à café de sucre ou<br>de miel au goût</li>
        <li>1-2 cuillères à café de gingembre<br>frais tranchés ou râpé (facultatif)</li>
      </ul>
    </div>
  </article>

  <article class="sachet sachet--ember-front pack--ember">
    <div class="pattern-band" role="img" aria-label="Dark brown leaf pattern texture"></div>
    <div class="seal">
      <p class="brand">Marlow Loft</p>
      <hr class="seal-rule">
      <h2 class="variety">Ember Blend</h2>
      <p class="desc">CHAI is a rich blend of strong and flavourful tea, aromatic spices, milk and sugar. Authentic Chai is an art that requires all natural ingredients, care and time to prepare.</p>
      <p class="desc">CHAI est un riche mélange de thé fort et savoureux, aromates, le lait et le sucre.</p>
    </div>
  </article>

  <article class="sachet sachet--ember-back pack--ember">
    <div class="recipe">
      <h3>INGREDIENTS /for 2 cups/:</h3>
      <ul>
        <li>1½ cups (12 oz) water.</li>
        <li>2 Chai tea bags.</li>
        <li>1 cup (8oz) (whole) milk.</li>
        <li>2-4 teaspoons sugar<br>or honey to taste</li>
        <li>1-2 teaspoons of sliced<br>or grated fresh ginger (optional)</li>
      </ul>
      <hr>
      <h3>INGRÉDIENTS /pour 2 tasses/:</h3>
      <ul>
        <li>1½ tasse (12 oz) d'eau.</li>
        <li>2 sachets de thé Chai.</li>
        <li>1 tasse (8 onces) (ensemble) lait.</li>
        <li>2-4 cuillères à café de sucre ou<br>de miel au goût</li>
        <li>1-2 cuillères à café de gingembre<br>frais tranchés ou râpé (facultatif)</li>
      </ul>
    </div>
  </article>

</main>
</body>
</html>
```